Bright Meadow Co - labels

I have my logo now so its time to proceed with the labels.
The product is organic juices and smoothies. They will be served in Mason jar's and sold as a premium hand made product into the CBD and outlets around Perth such as yoga studios gyms, cafe's etc. Cleanses to individuals etc.
I have attached the logo and a mock of what I would like to see.
I think the logo and the raw organic, handmade look will work with the Chalkboard design and maybe some bunting to brighten the design.
There is currently approx. 10 Juices and Smoothies to the range so I will need to settle on the design and then have you create a label for each one, once settled on the design.
If you have any questions please let me know.

Text on label:
Raw, Organic, Hand Made, Gluten-Free, Dairy-Free

Juice
Morning Vital Sip
Kale, Apple, Celery, Dandelion, Lemon & Ginger

This product is FRESH. Shake before you enjoy!!!

Label size. highest point for height 70 - 75mm. Length 200mm
I also have more wording and nutritional guide for Australian Standards. I will update soon.
Thank you

    Happy Friday Designers!!!

Well I have just increased the budget to $300. I hope this helps to get some designs coming through. If you need anything else from me please send a message.

I look forward to receiving your designs soon and thank you for working with me on my business. this is such an exciting time for me and you guys are making my dream a reality so thank you for your time.

Regards,

Tamsin

Reason: I have not received many designs so extending for a few more days.

Cafe

• Wording - Hand Made
Raw, Organic, Gluten-Free, Dairy-Free
• A chalk board with Juice or Smoothie - Name and ingredients
Bunting I think will work well with the design of logo and chalk board plus bring some colour.

```html
<!DOCTYPE html>
<html lang="en">
<head>
<meta charset="utf-8">
<title>Bright Meadow Co – Juice Label</title>
<link rel="stylesheet" href="https://fonts.googleapis.com/css2?family=Arvo:wght@700&family=Kalam:wght@400&family=Rubik+Dirt&family=Sacramento&family=Francois+One&display=swap">
<style>
  :root {
    --page: #efeae0;
    --chalkboard: #262626;
    --chalkboard-edge: #1b1b1b;
    --chalk-white: #f2f0ea;
    --orange: #d9631e;
    --orange-deep: #b8501a;
    --lime: #c9c41a;
    --silver-light: #f4f4f4;
    --silver-dark: #b9b9b9;
    --badge-white: #ffffff;
  }
  * { box-sizing: border-box; margin: 0; padding: 0; }
  html, body {
    width: 1200px;
    height: 900px;
    overflow: hidden;
    background: var(--page);
  }
  .canvas {
    position: relative;
    width: 1200px;
    height: 900px;
  }
  .label {
    position: absolute;
    left: 120px;
    top: 210px;
    width: 960px;
    height: 540px;
    background: radial-gradient(ellipse at 50% 40%, #313131 0%, var(--chalkboard) 60%, var(--chalkboard-edge) 100%);
    box-shadow: 0 10px 30px rgba(0,0,0,.25);
  }
  .label__trim {
    position: absolute;
    left: 0; right: 0; top: 0;
    height: 22px;
    background: linear-gradient(var(--silver-light), var(--silver-dark));
  }
  .bunting {
    position: absolute;
    top: 30px;
    height: 120px;
    width: 320px;
    background: linear-gradient(90deg, var(--orange) 0%, var(--lime) 50%, var(--orange) 100%);
    opacity: .85;
    clip-path: polygon(0 0, 100% 0, 100% 60%, 0 100%);
  }
  .bunting--left { left: 0; }
  .bunting--right { right: 0; clip-path: polygon(0 0, 100% 0, 100% 100%, 0 60%); }
  .brand-badge {
    position: absolute;
    left: 50%;
    top: -80px;
    width: 260px;
    height: 260px;
    margin-left: -130px;
    border-radius: 50%;
    background: var(--badge-white);
    box-shadow: 0 6px 14px rgba(0,0,0,.35);
    display: flex;
    align-items: center;
    justify-content: center;
    text-align: center;
  }
  .brand-badge__name {
    font-family: "Arvo", serif;
    font-weight: 700;
    font-size: 34px;
    line-height: 1.1;
    color: var(--orange);
    width: 200px;
  }
  .claims { position: absolute; font-family: "Kalam", cursive; font-size: 34px; text-transform: uppercase; letter-spacing: 1px; }
  .claims--handmade { left: 50px; top: 200px; color: var(--lime); transform: rotate(-4deg); }
  .claims--organic { right: 50px; top: 200px; color: var(--lime); transform: rotate(4deg); }
  .claims--gluten { left: 40px; top: 256px; color: var(--orange); transform: rotate(-9deg); }
  .claims--dairy { right: 40px; top: 256px; color: var(--orange); transform: rotate(9deg); }
  .claims--raw { left: 0; right: 0; top: 208px; text-align: center; color: var(--lime); }
  .claims__star { color: var(--orange); font-size: 30px; margin: 0 22px; }
  .product-name {
    position: absolute;
    left: 0; right: 0; top: 268px;
    text-align: center;
    font-family: "Sacramento", cursive;
    font-size: 64px;
    color: var(--chalk-white);
  }
  .product-type {
    position: absolute;
    left: 0; right: 0; top: 336px;
    text-align: center;
    font-family: "Rubik Dirt", sans-serif;
    font-size: 120px;
    line-height: 1;
    color: var(--orange);
    letter-spacing: 4px;
    text-shadow: 3px 3px 0 var(--chalk-white);
  }
  .ingredients {
    position: absolute;
    top: 350px;
    font-family: "Arvo", serif;
    font-weight: 700;
    font-size: 28px;
    line-height: 1.3;
    list-style: none;
    color: var(--lime);
  }
  .ingredients--left { left: 70px; text-align: left; }
  .ingredients--right { right: 70px; text-align: right; }
  .ingredients__item--light { color: var(--chalk-white); }
  .divider {
    position: absolute;
    left: 40px; right: 40px; top: 470px;
    border-top: 4px dotted var(--chalk-white);
  }
  .freshness-note {
    position: absolute;
    left: 0; right: 0; top: 484px;
    text-align: center;
    font-family: "Francois One", sans-serif;
    font-size: 30px;
    letter-spacing: 1px;
    color: var(--chalk-white);
    text-transform: uppercase;
  }
  .freshness-note__fresh {
    font-family: "Sacramento", cursive;
    text-transform: none;
    font-size: 40px;
    color: var(--lime);
  }
</style>
</head>
<body>
<main class="canvas">
  <section class="label">
    <div class="label__trim"></div>
    <div class="bunting bunting--left" role="img" aria-label="Bunting of orange and lime pennants"></div>
    <div class="bunting bunting--right" role="img" aria-label="Bunting of orange and lime pennants"></div>

    <div class="brand-badge">
      <span class="brand-badge__name">BRIGHT MEADOW CO</span>
    </div>

    <span class="claims claims--handmade">Handmade</span>
    <span class="claims claims--organic">Organic</span>
    <span class="claims claims--gluten">Gluten-Free</span>
    <span class="claims claims--dairy">Dairy-Free</span>
    <div class="claims claims--raw"><span class="claims__star">★</span>Raw<span class="claims__star">★</span></div>

    <h2 class="product-name">Morning Vital Sip</h2>
    <h1 class="product-type">JUICE</h1>

    <ul class="ingredients ingredients--left">
      <li>Kale</li>
      <li class="ingredients__item--light">Apple</li>
      <li>Celery</li>
    </ul>
    <ul class="ingredients ingredients--right">
      <li>Dandelion</li>
      <li>Lemon</li>
      <li>&amp; Ginger</li>
    </ul>

    <div class="divider"></div>
    <p class="freshness-note">This product is <span class="freshness-note__fresh">Fresh!</span> Shake before you enjoy!!!</p>
  </section>
</main>
</body>
</html>
```